App Design Project

We are building an app and looking for design help on an existing template. We will also need a style guide. For more information, there is a website which outlines the assignment with visuals. Go here:

http://www.brivalora.com/

Industry/Entity Type

Building

```html
<!DOCTYPE html>
<html lang="en">
<head>
<meta charset="utf-8">
<title>Activities</title>
<link rel="stylesheet" href="https://fonts.googleapis.com/css2?family=Oswald:wght@400;500;600&family=Arimo:wght@400;700&display=swap">
<style>
  :root {
    --page-bg: #e9e9e9;
    --header-top: #f4f5f5;
    --header-bottom: #a9b2b4;
    --red-light: #e0303a;
    --red-dark: #8e0a10;
    --olive-light: #8c7c3a;
    --olive-dark: #4a4118;
    --olive-border: #b59c3c;
    --blue-light: #4f87a6;
    --blue-dark: #1d4a63;
    --band-top: #ffffff;
    --band-bottom: #d7dadb;
    --card-top: #9a8f80;
    --card-bottom: #5e554a;
    --card-title: #2a2118;
    --card-sub: #3c2a10;
    --tile-bg: #0f1f2c;
    --tile-figure: #c9d3d8;
    --content-bg: #dedede;
    --gray-btn-light: #c9ccc4;
    --gray-btn-dark: #8f948a;
    --black-light: #3a3f44;
    --black-dark: #050607;
    --white: #ffffff;
    --chevron: #c2151c;
  }
  * { box-sizing: border-box; margin: 0; padding: 0; }
  html, body { width: 710px; height: 1200px; overflow: hidden; background: var(--page-bg); }
  .screen {
    position: absolute; left: 0; top: 67.5px;
    width: 320px; height: 480px;
    transform: scale(2.21875); transform-origin: 0 0;
    background: var(--content-bg);
    overflow: hidden;
    font-family: "Oswald", sans-serif;
  }
  .app-header {
    position: absolute; left: 0; top: 0; width: 320px; height: 82px;
    background: linear-gradient(var(--header-top), var(--header-bottom));
    border-bottom: 1px solid #8d9598;
  }
  .round-btn {
    position: absolute; top: 8px; width: 64px; height: 64px; border-radius: 50%;
    background: radial-gradient(circle at 50% 30%, var(--red-light), var(--red-dark) 80%);
    box-shadow: 0 1px 3px rgba(0,0,0,.45);
    color: var(--white); font-size: 17px; font-weight: 500;
    display: flex; align-items: center; justify-content: center; letter-spacing: .3px;
  }
  .round-btn.back { left: 5px; }
  .round-btn.sort { left: 253px; }
  .screen-title {
    position: absolute; left: 81px; top: 16px; width: 158px; height: 49px;
    border-radius: 18px; border: 1.5px solid var(--olive-border);
    background: linear-gradient(var(--olive-light), var(--olive-dark));
    color: var(--white); font-size: 17px; font-weight: 500;
    display: flex; align-items: center; justify-content: center; letter-spacing: .3px;
  }
  .filter-band {
    position: absolute; left: 0; top: 82px; width: 320px; height: 81px;
    background: linear-gradient(var(--band-top), var(--band-bottom));
    border-bottom: 1px solid #9da3a5;
  }
  .filter-pill {
    position: absolute; top: 24px; width: 92px; height: 30px; border-radius: 15px;
    background: linear-gradient(var(--blue-light), var(--blue-dark));
    box-shadow: 0 1px 2px rgba(0,0,0,.4);
    color: var(--white); font-size: 12px; font-weight: 400;
    display: flex; align-items: center; justify-content: center; letter-spacing: .2px;
  }
  .filter-pill.all { left: 9px; }
  .filter-pill.people { left: 112px; }
  .filter-pill.groups { left: 215px; }
  .event-card {
    position: absolute; left: 0; top: 163px; width: 320px; height: 140px;
    background: linear-gradient(var(--card-top), #857a6b 45%, var(--card-bottom));
    border-bottom: 1px solid #4a4238;
  }
  .event-title {
    position: absolute; left: 8px; top: 20px;
    font-size: 20px; font-weight: 600; color: var(--card-title); letter-spacing: .2px;
  }
  .event-venue, .event-date {
    position: absolute; left: 9px; font-size: 13px; font-weight: 500; color: var(--card-sub);
  }
  .event-venue { top: 49px; }
  .event-date { top: 72px; }
  .event-expiry {
    position: absolute; left: 8px; top: 106px;
    font-family: "Arimo", sans-serif; font-size: 12px; color: var(--white);
  }
  .host-tile {
    position: absolute; left: 236px; top: 52px; width: 56px; height: 58px;
    border-radius: 4px; border: 1px solid #6d7f8a;
    background: linear-gradient(#1d3243, var(--tile-bg));
  }
  .host-avatar {
    position: absolute; left: 17px; top: 8px; width: 22px; height: 42px;
    border-radius: 3px; background: var(--tile-figure); opacity: .85;
  }
  .host-name {
    position: absolute; left: 226px; top: 114px; width: 76px; text-align: center;
    font-family: "Arimo", sans-serif; font-size: 10px; color: var(--white);
  }
  .chevron { position: absolute; left: 299px; top: 73px; width: 10px; height: 14px; }
  .tab-bar { position: absolute; left: 0; top: 417px; width: 320px; height: 52px; }
  .tab {
    position: absolute; top: 0; width: 57px; height: 52px; border-radius: 4px;
    color: var(--white); font-size: 14px; font-weight: 400; line-height: 1.05;
    display: flex; align-items: center; justify-content: center; text-align: center;
    box-shadow: 0 1px 2px rgba(0,0,0,.35); letter-spacing: .2px;
  }
  .tab.search { left: 7px; background: linear-gradient(var(--olive-light), var(--olive-dark)); border: 1px solid var(--olive-border); }
  .tab.new-posts { left: 69px; background: linear-gradient(var(--gray-btn-light), var(--gray-btn-dark)); border: 1px solid #aeb2a8; }
  .tab.messages { left: 132px; background: linear-gradient(var(--blue-light), var(--blue-dark)); }
  .tab.alerts { left: 194px; background: linear-gradient(var(--black-light), var(--black-dark)); }
  .tab.more { left: 256px; background: linear-gradient(var(--red-light), var(--red-dark)); }
</style>
</head>
<body>
  <main class="screen">
    <header class="app-header">
      <div class="round-btn back">BACK</div>
      <h1 class="screen-title">ACTIVITIES</h1>
      <div class="round-btn sort">SORT</div>
    </header>

    <nav class="filter-band">
      <div class="filter-pill all">SEARCH ALL</div>
      <div class="filter-pill people">PEOPLE</div>
      <div class="filter-pill groups">GROUPS</div>
    </nav>

    <article class="event-card">
      <h2 class="event-title">MIDNIGHT HORROR SHOW</h2>
      <p class="event-venue">OLD TOWN CINEMA</p>
      <p class="event-date">OCTOBER 8, 2012, 12.00AM</p>
      <p class="event-expiry">Expires in 6hrs, 39 mins</p>
      <div class="host-tile">
        <div class="host-avatar" role="img" aria-label="Host profile icon"></div>
      </div>
      <p class="host-name">NANCY 14</p>
      <svg class="chevron" viewBox="0 0 10 14" aria-hidden="true">
        <polyline points="2,1.5 8,7 2,12.5" fill="none" stroke="var(--chevron)" stroke-width="2"/>
      </svg>
    </article>

    <footer class="tab-bar">
      <div class="tab search">SEARCH</div>
      <div class="tab new-posts">NEW<br>POSTS</div>
      <div class="tab messages">MSGS</div>
      <div class="tab alerts">ALERTS</div>
      <div class="tab more">MORE</div>
    </footer>
  </main>
</body>
</html>
```